Non-Profit, Organic, Natural Feel, Clean & Simple Business Cards

Looking for a business card design. Has an organic, natural, new-age, clean and simple look/feel. We are a non-profit group that works with Moringa(a health plant/superfood) by spreading and sharing seeds of Moringa. A design that stands out but clean and professional. I will upload our new logo design. The font can be changed. Also I will upload some pictures of Moringa.
Our Facebook page is www.facebook.com/TulvaSproutTrust Check us out to get a feel of us.

Target Market(s)

Everyone. Movers & Shakers of The Sustainable, Natural Medicines & Cosmetics, Organic Food Farming Industry. And To The Common Person Or A Local Family.

Industry/Entity Type

Sustainability

Contact Information for Business Card

Email: TulvaSoilTrust@Brenwick.com
FB: www.Facebook.com/TulvaSproutTrust
Website: www.TulvaSproutTrust.com

Requirements
Must have
• Image/Pic/Design of Moringa Leaves. Somewhere on the card. Clean and Clear. So you could easily identify the Moringa from the Business Card. Something Alive, Living, Green Feel to the card design.
Nice to have
• A warm, friendly, professional feel to the design. A organic sustainable concept/future with Moringa is the business card impression/image we are trying to present.

```html
<!DOCTYPE html>
<html lang="en">
<head>
<meta charset="utf-8">
<title>Tulva Sprout Trust — Business Card</title>
<link rel="stylesheet" href="https://fonts.googleapis.com/css2?family=Open+Sans:wght@400;600;700&display=swap">
<style>
  :root {
    --leaf-green: #5cc21a;
    --lime: #6fd60a;
    --lime-deep: #5cbf06;
    --name-green: #4caf14;
    --icon-green: #3aa32a;
    --ink: #222;
    --paper: #ffffff;
    --backdrop: #eeeeea;
  }
  html, body {
    margin: 0;
    width: 1200px;
    height: 900px;
    overflow: hidden;
    background: var(--backdrop);
    font-family: "Open Sans", Arial, sans-serif;
  }
  .stage { position: relative; width: 1200px; height: 900px; }

  .card {
    position: absolute;
    box-sizing: border-box;
    background: var(--leaf-green);
    box-shadow: 0 6px 18px rgba(0,0,0,.18);
  }
  .card--front { left: 78px; top: 35px; width: 588px; height: 364px; padding: 30px 32px 30px 28px; }
  .card--back  { left: 388px; top: 507px; width: 566px; height: 350px; padding: 28px 32px 28px 24px; }

  .card__panel {
    position: relative;
    width: 100%;
    height: 100%;
    overflow: hidden;
    border-radius: 10px;
    box-shadow: inset 0 0 0 2px rgba(0,0,0,.06);
  }
  .card--front .card__panel { background: var(--paper); }
  .card--back .card__panel {
    background: linear-gradient(180deg, var(--lime) 0%, var(--lime-deep) 100%);
  }

  .leaf-art {
    position: absolute;
    left: 19px;
    top: 60px;
    width: 205px;
    height: 236px;
    border-radius: 50% 50% 8px 50%;
    background: radial-gradient(ellipse at 55% 40%, #7fd06a 0%, #4fb84a 60%, #3fa83a 100%);
    opacity: .9;
  }

  .identity { position: absolute; left: 249px; top: 82px; }
  .identity__name { margin: 0; font-size: 20px; font-weight: 700; color: var(--name-green); line-height: 1.2; }
  .identity__role { margin: 1px 0 0; font-size: 15px; color: var(--ink); line-height: 1.3; }

  .contacts {
    position: absolute;
    left: 249px;
    top: 164px;
    margin: 0;
    padding: 0;
    list-style: none;
    font-size: 15px;
    color: var(--ink);
  }
  .contacts li { display: flex; align-items: center; height: 24px; }
  .contacts svg { width: 12px; height: 12px; margin-right: 13px; flex: none; }

  .brand {
    position: absolute;
    inset: 0;
    display: flex;
    align-items: center;
    justify-content: center;
    gap: 16px;
    color: var(--paper);
  }
  .brand__square { width: 40px; height: 40px; background: var(--paper); flex: none; }
  .brand__name { font-size: 34px; font-weight: 400; letter-spacing: 3px; }
</style>
</head>
<body>
<main class="stage">
  <section class="card card--front" aria-label="Card front">
    <div class="card__panel">
      <div class="leaf-art" role="img" aria-label="Illustration of a green moringa leaf sprig"></div>
      <div class="identity">
        <p class="identity__name">Maren Okafor</p>
        <p class="identity__role">Managing Director</p>
      </div>
      <ul class="contacts">
        <li>
          <svg viewBox="0 0 12 12" aria-hidden="true"><path fill="var(--icon-green)" d="M2.5 1l2 2.2-1 1.3a7 7 0 0 0 4 4l1.3-1L11 9.5 9.6 11C5 11 1 7 1 2.4z"/></svg>
          (044)-318-2264
        </li>
        <li>
          <svg viewBox="0 0 12 12" aria-hidden="true"><rect x="1" y="2.5" width="10" height="7" fill="var(--icon-green)"/><path d="M1 2.5l5 4 5-4" stroke="#fff" fill="none"/></svg>
          TulvaSoilTrust@Brenwick.com
        </li>
        <li>
          <svg viewBox="0 0 12 12" aria-hidden="true"><circle cx="6" cy="6" r="5" fill="var(--icon-green)"/><circle cx="6" cy="6" r="2" fill="#fff"/></svg>
          www.TulvaSproutTrust.com
        </li>
        <li>
          <svg viewBox="0 0 12 12" aria-hidden="true"><circle cx="6" cy="6" r="3" fill="var(--icon-green)"/></svg>
          TulvaSproutTrust
        </li>
      </ul>
    </div>
  </section>

  <section class="card card--back" aria-label="Card back">
    <div class="card__panel">
      <div class="brand">
        <span class="brand__square" aria-hidden="true"></span>
        <span class="brand__name">TULVA SPROUT TRUST</span>
      </div>
    </div>
  </section>
</main>
</body>
</html>
```